Bref créative
Norland Equity Partners
Investing
Professional
Tom Radcliffe
President
728 Maplewood Ave. Suite 310
Oak Terrace, CA 90418
tom@NorlandEquityPartners.com
www.NorlandEquityPartners.com
We want our logo to be the main component of the card. Have fun and let me see what you got!
Feel free to try 1 or 2 sided card ideas.
Can use other fonts besides the logo font if you desire.

```html
<!DOCTYPE html>
<html lang="en">
<head>
<meta charset="utf-8">
<title>Norland Equity Partners — Stationery</title>
<link rel="stylesheet" href="https://fonts.googleapis.com/css2?family=Montserrat:wght@400;600;700&display=swap">
<style>
  :root{
    --stage:#8f9194;
    --paper:#ffffff;
    --red:#e8202a;
    --ink:#2b2b2b;
    --slate:#3a3a3c;
    --muted:#6d6d6d;
    --ghost:#f2eeee;
  }
  *{margin:0;padding:0;box-sizing:border-box}
  html,body{width:1200px;height:697px;overflow:hidden}
  body{background:var(--stage);font-family:"Montserrat",Arial,sans-serif;position:relative}
  .sheet{position:absolute;background:var(--paper);box-shadow:0 1px 4px rgba(0,0,0,.25)}

  .brand{display:flex;align-items:center;gap:8px}
  .brand__dot{border-radius:50%;background:var(--red);flex:none}
  .brand__name{font-weight:700;color:var(--ink);white-space:nowrap}

  /* Business card */
  .card{left:19px;top:317px;width:192px;height:110px;background:var(--slate);overflow:hidden;border-radius:3px}
  .card__curve{position:absolute;inset:0}
  .card__brand{position:absolute;left:10px;top:18px}
  .card__brand .brand__dot{width:14px;height:14px}
  .card__brand .brand__name{font-size:6.4px}
  .card__tag{position:absolute;right:0;top:12px;width:80px;height:26px;background:var(--red);padding:4px 8px;text-align:right;color:#fff}
  .card__person{font-size:8px;font-weight:600;line-height:1.1}
  .card__role{font-size:5px}
  .card__contact{position:absolute;left:10px;bottom:10px;color:#e6e6e6;font-size:4.4px;line-height:1.5}

  /* Letterhead */
  .letterhead{left:216px;top:29px;width:403px;height:629px}
  .letterhead__brand{position:absolute;left:26px;top:28px}
  .letterhead__brand .brand__dot{width:26px;height:26px}
  .letterhead__brand .brand__name{font-size:10px}
  .letterhead__contact{position:absolute;right:22px;top:20px;text-align:right;font-size:7px;line-height:1.75;color:var(--muted)}
  .letterhead__mark{position:absolute;left:50%;top:340px;transform:translateX(-50%);opacity:.09}
  .letterhead__mark .brand__dot{width:80px;height:80px}
  .letterhead__mark .brand__name{font-size:24px}

  /* Envelope */
  .envelope-front{left:672px;top:235px;width:456px;height:168px}
  .envelope-front__brand{position:absolute;left:20px;top:82px}
  .envelope-front__brand .brand__dot{width:18px;height:18px}
  .envelope-front__brand .brand__name{font-size:7.5px}
  .envelope-back{left:672px;top:413px;width:456px;height:242px}
  .envelope-back__flap{position:absolute;left:0;top:0;width:100%;height:90px}
</style>
</head>
<body>

  <section class="sheet card" aria-label="Business card">
    <svg class="card__curve" viewBox="0 0 192 110" preserveAspectRatio="none" aria-hidden="true">
      <path d="M0 0 H120 C95 20 92 45 112 70 C80 72 40 68 0 74 Z" fill="var(--paper)"/>
    </svg>
    <div class="brand card__brand"><span class="brand__dot"></span><span class="brand__name">Norland Equity Partners</span></div>
    <div class="card__tag">
      <p class="card__person">Tom Radcliffe</p>
      <p class="card__role">President</p>
    </div>
    <address class="card__contact" style="font-style:normal">
      728 Maplewood Ave. Suite 310<br>Oak Terrace, CA 90418<br>tom@NorlandEquityPartners.com<br>www.NorlandEquityPartners.com
    </address>
  </section>

  <section class="sheet letterhead" aria-label="Letterhead">
    <div class="brand letterhead__brand"><span class="brand__dot"></span><span class="brand__name">Norland Equity Partners</span></div>
    <address class="letterhead__contact" style="font-style:normal">
      www.NorlandEquityPartners.com<br>
      Phone: 310-555-0148<br>
      Email: tom@NorlandEquityPartners.com<br>
      728 Maplewood Ave. Suite 310 Oak Terrace, CA 90418
    </address>
    <div class="brand letterhead__mark" aria-hidden="true"><span class="brand__dot"></span><span class="brand__name">Norland Equity Partners</span></div>
  </section>

  <section class="sheet envelope-front" aria-label="Envelope front">
    <div class="brand envelope-front__brand"><span class="brand__dot"></span><span class="brand__name">Norland Equity Partners</span></div>
  </section>

  <section class="sheet envelope-back" aria-label="Envelope back">
    <svg class="envelope-back__flap" viewBox="0 0 456 90" preserveAspectRatio="none" aria-hidden="true">
      <path d="M0 0 H456 V8 L420 80 Q416 88 406 88 H50 Q40 88 36 80 L0 8 Z" fill="var(--red)"/>
    </svg>
  </section>

</body>
</html>
```